*** Business Card Design Project

I need a logo and business card for my new catering business: "Pomelia". The design should be modern, clean, elegant and refined. One or Two colours only. The design SHOULD NOT include graphics or images. There should be space for my name, phone number and email address (I will provide these to you later).

Industry/Entity Type

Catering

Requirements
Must have
• Must have one or two colours only.
Must include the text "pomelia"
Should not have
• Must not have graphics or images.

```html
<!DOCTYPE html>
<html lang="en">
<head>
<meta charset="utf-8">
<title>Pomelia — business card studies</title>
<link rel="stylesheet" href="https://fonts.googleapis.com/css2?family=Antonio:wght@100;300&display=swap">
<style>
  :root {
    --sage: #8fa865;
    --ink: #666666;
    --paper: #ffffff;
    --edge: #c9c9c9;
    --page: #ffffff;
  }
  * { margin: 0; padding: 0; box-sizing: border-box; }
  html, body {
    width: 1200px; height: 692px; overflow: hidden;
    background: var(--page);
  }
  .sheet { position: relative; width: 1200px; height: 692px; }
  .card {
    position: absolute; width: 583px; height: 330px;
    background: var(--paper); border: 2px solid var(--edge);
    overflow: hidden;
  }
  .card svg { display: block; width: 579px; height: 326px; }
  .card--stacked  { left: 7px;   top: 7px; }
  .card--centered { left: 610px; top: 7px; }
  .card--spaced   { left: 7px;   top: 357px; }
  .card--tilted   { left: 610px; top: 357px; }

  .wordmark {
    font-family: "Antonio", "Arial Narrow", sans-serif;
    font-weight: 100;
    fill: var(--sage);
  }
  .contact {
    font-family: "Antonio", "Arial Narrow", sans-serif;
    font-weight: 300;
    fill: var(--ink);
  }
  .contact .accent { fill: var(--sage); }
</style>
</head>
<body>
<main class="sheet">
  <section class="card card--stacked">
    <svg viewBox="0 0 579 326" aria-label="pomelia card, stacked layout">
      <text class="wordmark" x="82" y="166" font-size="158" textLength="409" lengthAdjust="spacing">pomelia</text>
      <text class="contact" x="86" y="222" font-size="19" textLength="339" lengthAdjust="spacing">nora hale <tspan class="accent">555.014.2280</tspan> n.hale@pomelia.com</text>
      <text class="contact" x="86" y="250" font-size="19" textLength="390" lengthAdjust="spacing">www.pomeliacatering.com <tspan class="accent">ASHFORD, VERMONT</tspan></text>
    </svg>
  </section>

  <section class="card card--centered">
    <svg viewBox="0 0 579 326" aria-label="pomelia card, centered layout">
      <text class="wordmark" x="96" y="192" font-size="168" textLength="385" lengthAdjust="spacing">pomelia</text>
      <text class="contact" x="61" y="290" font-size="19" textLength="451" lengthAdjust="spacing">nora hale <tspan class="accent">555.014.2280</tspan> n.hale@pomelia.com</text>
      <text class="contact" x="49" y="317" font-size="19" textLength="469" lengthAdjust="spacing">www.pomeliacatering.com <tspan class="accent">ASHFORD, VERMONT</tspan></text>
    </svg>
  </section>

  <section class="card card--spaced">
    <svg viewBox="0 0 579 326" aria-label="pomelia card, letterspaced layout">
      <text class="wordmark" x="140" y="180" font-size="70" textLength="287" lengthAdjust="spacing">pomelia</text>
      <text class="contact" x="98" y="224" font-size="19" textLength="383" lengthAdjust="spacing">nora hale <tspan class="accent">555.014.2280</tspan> n.hale@pomelia.com</text>
      <text class="contact" x="98" y="258" font-size="19" textLength="385" lengthAdjust="spacing">www.pomeliacatering.com <tspan class="accent">ASHFORD, VERMONT</tspan></text>
    </svg>
  </section>

  <section class="card card--tilted">
    <svg viewBox="0 0 579 326" aria-label="pomelia card, angled layout">
      <g transform="translate(14 244) rotate(-17)">
        <text class="wordmark" x="10" y="-36" font-size="124" textLength="420" lengthAdjust="spacing">pomelia</text>
        <text class="contact" x="0" y="0" font-size="16" textLength="449" lengthAdjust="spacing">nora hale <tspan class="accent">555.014.2280</tspan> n.hale@pomelia.com <tspan class="accent">ashford, vermont</tspan></text>
      </g>
    </svg>
  </section>
</main>
</body>
</html>
```